Need Primer (paint) Label Design

THE ATTACHED LABEL/S ARE SOLEY FOR REFERENCE. DO NOT MAKE ME AN INTERIOR PAINT OR CHALK PAINT LABEL. I ONLY NEED A "PRIMER" LABEL. THE ATTACHED INTERIOR PAINT LABEL IS ONLY TO SHOW YOU THE THEME/DESIGN OF OUR OTHER LABELS. THE BLUE LABEL ONLY HAS A DESIGN ASPECT I LIKE (PRIMER ON SIDE). The last four labels are our competitors.
```````````````````````````````````````````````````````````````````````````````````````````````````
We need this label to look professional, sharp, eye catching and modern.
OUR PRIMARY COLORS ARE BLACK AND WHITE. IF YOU INCOPORATE ANOTHER COLOR, SILVER OR GOLD MIGHT BE IDEAL BUT PLEASE DON'T DRIFT TOO FAR.
The attached documents:
1st - Our Logo
2nd - Our chalk paint label (reference). We do not need a chalk paint label.
3rd. A random design example. I like the PRIME on the side running vertically. I think it's a cool design concept.
````````````````````````````````````````````````````````````````````````````````````````````````````
We are going to be using a normal paint can with a metal bail/handle so please use that with you design work
``````````````````````````````````````````````````````````````````````````````````````````````````
Order, in my head:
2743
Coatings
^^ I want this to stand out as well but I don't want it to be the first thing your eye is drawn to. Probably 2nd
Interior/Exterior
Multi - Surface Primer
^^ Want this to stick out and draw your eye so the customer knows what it is immediately
Exceptional Adhesion, Performance, Durability,
Use on Wood, Drywall, Plaster, Stucco, Masonry, Brick, Paneling, Painted Metal, & Properly Prepared Glossy Surfaces & More
35* Lowe Temperature Application (can be on side or small)
100% Acrylic
Low Odor - Low VOC - Soap & Water Clean Up
1 US Gallon - 3.785 L
Feel free to get creative with it!

```html
<!DOCTYPE html>
<html lang="en">
<head>
<meta charset="utf-8">
<title>2743 Coatings – Multi-Surface Primer Label</title>
<link rel="stylesheet" href="https://fonts.googleapis.com/css2?family=Bebas+Neue&family=Jost:wght@400&family=Montserrat:wght@800&family=Oswald:wght@200;300&display=swap">
<style>
  :root {
    --label-black: #000000;
    --label-white: #ffffff;
  }
  html, body {
    margin: 0;
    padding: 0;
    width: 1200px;
    height: 412px;
    overflow: hidden;
    background: var(--label-black);
  }
  .primer-label {
    display: block;
    width: 1200px;
    height: 412px;
    background: var(--label-black);
  }
  .frame {
    fill: none;
    stroke: var(--label-white);
    stroke-width: 3;
  }
  .tag-band { fill: var(--label-white); }
  .txt { fill: var(--label-white); }
  .condensed-light { font-family: "Oswald", sans-serif; }
  .condensed-bold { font-family: "Bebas Neue", sans-serif; font-weight: 400; }
  .surface-list { font-weight: 300; font-size: 22px; }
  .side-word { font-family: "Jost", sans-serif; font-weight: 400; font-size: 82px; fill: var(--label-white); }
  .brand-name { font-size: 42px; }
  .product-type { font-family: "Montserrat", sans-serif; font-weight: 800; font-size: 16px; fill: var(--label-white); }
  .product-sub { font-family: "Montserrat", sans-serif; font-weight: 800; font-size: 12.5px; fill: var(--label-white); }
  .tag-text { font-family: "Bebas Neue", sans-serif; font-size: 27px; fill: var(--label-black); }
  .volume { font-size: 27px; }
  .tagline { font-size: 32px; }
  .feature-small { font-size: 18px; }
  .feature-bold { font-size: 27px; }
  .feature-light { font-weight: 200; font-size: 35px; }
  .feature-heavy { font-size: 38px; }
  .feature-clean { font-weight: 200; font-size: 27px; }
</style>
</head>
<body>
<svg class="primer-label" viewBox="0 0 1200 412" xmlns="http://www.w3.org/2000/svg" role="img" aria-label="2743 Coatings interior/exterior multi-surface primer label">

  <g class="surfaces-panel">
    <rect class="frame" x="93.5" y="57.5" width="227" height="227"/>
    <text class="txt condensed-light surface-list" lengthAdjust="spacingAndGlyphs">
      <tspan x="114" y="122" textLength="158" lengthAdjust="spacingAndGlyphs">Use on Wood, Drywall,</tspan>
      <tspan x="114" y="152" textLength="173" lengthAdjust="spacingAndGlyphs">Plaster, Stucco, Masonry,</tspan>
      <tspan x="114" y="182" textLength="165" lengthAdjust="spacingAndGlyphs">Brick, Paneling, Painted</tspan>
      <tspan x="114" y="212" textLength="186" lengthAdjust="spacingAndGlyphs">Metal, &amp; Properly Prepared</tspan>
      <tspan x="114" y="242" textLength="161" lengthAdjust="spacingAndGlyphs">Glossy Surfaces &amp; More</tspan>
    </text>
  </g>

  <text class="side-word" transform="translate(373 59) rotate(90)" x="0" y="0" textLength="239">Primer</text>

  <g class="brand-panel">
    <rect class="frame" x="486.5" y="57.5" width="227" height="227"/>
    <text class="txt condensed-bold brand-name" x="600" y="166" text-anchor="middle" textLength="176" lengthAdjust="spacingAndGlyphs">2743 COATINGS</text>
    <text class="product-type" x="600" y="231" text-anchor="middle" textLength="183" lengthAdjust="spacingAndGlyphs">INTERIOR/EXTERIOR</text>
    <text class="product-sub" x="600" y="249" text-anchor="middle" textLength="196" lengthAdjust="spacingAndGlyphs">MULTI - SURFACE PRIMER</text>
    <rect class="tag-band" x="515" y="269" width="168" height="28"/>
    <text class="tag-text" x="600" y="294" text-anchor="middle" textLength="64" lengthAdjust="spacingAndGlyphs">PRIMER</text>
    <text class="txt condensed-bold volume" x="600" y="327" text-anchor="middle" textLength="182" lengthAdjust="spacingAndGlyphs">1 US GALLON - 3.785 L</text>
  </g>

  <text class="side-word" transform="translate(855 298) rotate(-90)" x="0" y="0" textLength="239">Primer</text>

  <g class="features-panel">
    <rect class="frame" x="924.5" y="57.5" width="227" height="227"/>
    <text class="txt condensed-bold feature-small" x="1038" y="97" text-anchor="middle" textLength="213" lengthAdjust="spacingAndGlyphs">35* LOWE TEMPERATURE APPLICATION</text>
    <text class="txt condensed-bold feature-bold" x="1036" y="133" text-anchor="middle" textLength="127" lengthAdjust="spacingAndGlyphs">100 % ACRYLIC</text>
    <text class="txt condensed-light feature-light" x="1037" y="178" text-anchor="middle" textLength="111" lengthAdjust="spacingAndGlyphs">LOW ODOR</text>
    <text class="txt condensed-bold feature-heavy" x="1037" y="221" text-anchor="middle" textLength="97" lengthAdjust="spacingAndGlyphs">LOW VOC</text>
    <text class="txt condensed-light feature-clean" x="1037" y="257" text-anchor="middle" textLength="202" lengthAdjust="spacingAndGlyphs">SOAP &amp; WATER CLEAN UP</text>
  </g>

  <text class="txt condensed-bold tagline" x="599" y="374" text-anchor="middle" textLength="494" lengthAdjust="spacingAndGlyphs" xml:space="preserve">EXCEPTIONAL ADHESION  PERFORMANCE  DURABILITY</text>
</svg>
</body>
</html>
```